New branding for a sponsored social ad network

We're seeking a new corporate branding for our sponsored social ad network.

We deliver over 6 million clicks per day off of lumiport and zonvel to brands, game and app companies, musicians and a host of other content and product producers seeking to get the right eyeballs on their content.

Our current design and a little information about our company can be seen at http://qv.lo/pmTHza

An example of a competitor site we'd like to closely resemble in look and feel can be seen at http://qv.lo/82GvR4k

Industry/Entity Type

It Company

```html
<!DOCTYPE html>
<html lang="en">
<head>
<meta charset="utf-8">
<title>Vocalift — Sponsored Social Ad Network</title>
<link href="https://fonts.googleapis.com/css2?family=Oxygen:wght@400;700&family=Rye&display=swap" rel="stylesheet">
<style>
  :root{
    --black:#0b0b0b;
    --bar-top:#2a2a2a;
    --cyan:#2ec4f0;
    --green:#6cc417;
    --green-line:#77c520;
    --blue-box:#2f86f2;
    --blue-box-deep:#1f6fe8;
    --band-left:#3a4fc4;
    --band-right:#5d74d2;
    --white:#ffffff;
  }
  *{box-sizing:border-box;margin:0;padding:0}
  html,body{width:1200px;height:720px;overflow:hidden;background:var(--black)}
  body{font-family:"Oxygen",Verdana,sans-serif;color:var(--white);position:relative}

  .site-header{position:absolute;left:0;top:0;width:1200px;height:79px;
    background:linear-gradient(#050505,var(--bar-top));border-bottom:3px solid var(--green-line)}
  .brand{position:absolute;left:22px;top:12px;display:flex;align-items:center;gap:8px;
    font-size:38px;font-weight:400;color:var(--cyan);letter-spacing:0.5px}
  .brand-dot{width:16px;height:16px;border-radius:50%;background:var(--cyan)}
  .top-nav{position:absolute;right:22px;top:32px;display:flex;gap:20px}
  .top-nav a{color:var(--cyan);text-decoration:none;font-size:24px;font-variant:small-caps}

  .hero{position:absolute;left:0;top:79px;width:1200px;height:355px;overflow:hidden}
  .hero-collage{position:absolute;inset:0;
    background:
      linear-gradient(90deg,rgba(120,150,90,.55) 0%,rgba(90,100,110,.4) 20%,rgba(200,200,195,.35) 55%,rgba(180,150,110,.4) 78%,rgba(200,170,120,.5) 100%),
      linear-gradient(180deg,#8f9aa0 0%,#c6c2bb 45%,#5d6460 75%,#4a4c48 100%)}
  .hero-card{position:absolute;left:74px;top:16px;width:569px;height:221px;background:var(--blue-box);
    box-shadow:0 0 0 1px rgba(255,255,255,.4)}
  .hero-card::before{content:"";position:absolute;inset:7px;border:1.5px solid rgba(255,255,255,.85)}
  .hero-title{position:absolute;left:28px;top:14px;font-family:"Rye",serif;font-size:66px;
    font-weight:400;letter-spacing:3px;color:var(--white)}
  .hero-text{position:absolute;left:23px;top:118px;width:530px;font-size:20px;line-height:25px}
  .btn{display:inline-block;background:var(--green);color:var(--white);border-radius:3px;
    font-family:"Oxygen",Verdana,sans-serif;text-align:center}
  .hero-btn{position:absolute;left:20px;top:189px;width:200px;height:33px;line-height:33px;font-size:17px}
  .slide-arrow{position:absolute;top:0;width:100%;height:100%;pointer-events:none}
  .rule{position:absolute;left:0;top:434px;width:1200px;height:3px;background:var(--green-line)}

  .feature-band{position:absolute;left:0;top:437px;width:1200px;height:233px;
    background:linear-gradient(100deg,var(--band-left),var(--band-right))}
  .signup{position:absolute;left:19px;top:13px}
  .email-field{position:absolute;left:0;top:0;width:237px;height:26px;background:var(--white);
    border-radius:3px;color:#9a9a9a;font-size:16px;line-height:26px;padding-left:8px}
  .signup-btn{position:absolute;left:257px;top:0;width:161px;height:26px;line-height:26px;font-size:17px}
  .signup-note{position:absolute;left:1px;top:34px;white-space:nowrap;font-size:13.5px}
  .feature{position:absolute;top:78px}
  .feature-left{left:163px}
  .feature-right{left:628px}
  .feature h2{font-size:30px;font-weight:700;font-variant:small-caps;letter-spacing:.5px;line-height:34px}
  .feature h2 .accent{color:var(--green)}
  .feature ul{list-style:none;margin-top:4px}
  .feature li{display:flex;align-items:center;height:31px;font-size:17.5px}
  .tick{width:18px;height:24px;margin-right:4px;flex:none}

  .site-footer{position:absolute;left:0;top:670px;width:1200px;height:50px;
    background:linear-gradient(#1a1a1a,var(--black));border-top:2px solid #3a3a3a}
  .footer-nav a{position:absolute;top:14px;color:var(--white);text-decoration:none;
    font-size:23px;font-variant:small-caps}
  .footer-brand{position:absolute;right:16px;top:10px;font-size:24px;color:var(--cyan)}
</style>
</head>
<body>
  <header class="site-header">
    <div class="brand"><span>Vocalift</span><span class="brand-dot"></span></div>
    <nav class="top-nav">
      <a href="#">About Us</a><a href="#">Sign Up</a><a href="#">Login</a>
    </nav>
  </header>

  <section class="hero">
    <div class="hero-collage" role="img" aria-label="Collage of blog screenshots and photographs with sticky notes reading Analytics, Active Campaign and Referring Traffic Sources"></div>
    <div class="hero-card">
      <h1 class="hero-title">PUBLISHERS</h1>
      <p class="hero-text">Earn money posting sponsored tweets, lumiport updates and blog entries about things you love.</p>
      <span class="btn hero-btn">Start my campaign!</span>
    </div>
    <svg class="slide-arrow" viewBox="0 0 1200 355" aria-hidden="true">
      <circle cx="-28" cy="179" r="65" fill="#6cc417"/>
      <polyline points="24,157 5,179 24,201" fill="none" stroke="#fff" stroke-width="4"/>
      <circle cx="1221" cy="179" r="65" fill="#6cc417"/>
      <polyline points="1175,157 1194,179 1175,201" fill="none" stroke="#fff" stroke-width="4"/>
    </svg>
  </section>
  <div class="rule"></div>

  <section class="feature-band">
    <div class="signup">
      <div class="email-field">Enter email...</div>
      <span class="btn signup-btn">Sign up!</span>
      <p class="signup-note">We will create your account and email password instructions.</p>
    </div>

    <div class="feature feature-left">
      <h2><span class="accent">Promote</span> Your Video</h2>
      <ul>
        <li><svg class="tick" viewBox="0 0 18 24"><polyline points="2,14 7,22 16,2" fill="none" stroke="#6cc417" stroke-width="1.6"/></svg>Reach out to relevant consumers.</li>
        <li><svg class="tick" viewBox="0 0 18 24"><polyline points="2,14 7,22 16,2" fill="none" stroke="#6cc417" stroke-width="1.6"/></svg>Target audiences by demographics.</li>
        <li><svg class="tick" viewBox="0 0 18 24"><polyline points="2,14 7,22 16,2" fill="none" stroke="#6cc417" stroke-width="1.6"/></svg>Lower cost per click.</li>
      </ul>
    </div>

    <div class="feature feature-right">
      <h2><span class="accent">Join</span> Our Publisher Network</h2>
      <ul>
        <li><svg class="tick" viewBox="0 0 18 24"><polyline points="2,14 7,22 16,2" fill="none" stroke="#6cc417" stroke-width="1.6"/></svg>Earn great money posting fun and interesting content.</li>
        <li><svg class="tick" viewBox="0 0 18 24"><polyline points="2,14 7,22 16,2" fill="none" stroke="#6cc417" stroke-width="1.6"/></svg>Convert followers on lumiport or zonvel into customers.</li>
        <li><svg class="tick" viewBox="0 0 18 24"><polyline points="2,14 7,22 16,2" fill="none" stroke="#6cc417" stroke-width="1.6"/></svg>Maximize and expand your web presence.</li>
      </ul>
    </div>
  </section>

  <footer class="site-footer">
    <nav class="footer-nav">
      <a href="#" style="left:17px">Contact</a>
      <a href="#" style="left:164px">About Us</a>
      <a href="#" style="left:323px">Blog</a>
      <a href="#" style="left:440px">Faqs</a>
      <a href="#" style="left:553px">Login</a>
    </nav>
    <div class="footer-brand">Vocalift</div>
  </footer>
</body>
</html>
```